Coffee House With Cycling Theme Wants Business Cards

We want to create a business card for a coffee house that has a cycling theme. We expect to use the current logo on one side of the business card and we have been considering adding the words 'COFFEE HOUSE' underneath (see example). For the other side of the business card we want an interesting design with tag-line, address and social media links (the normal business card stuff). See examples provided but we are not fixed on having it exactly as shown, we are very open to great creative ideas. Please note our logo has the initials ‘RM' in orange embedded in the design and this must be retained. However, you can play with the words COFFEE HOUSE as well as use the orange color on the backside of the business card, as you see fit. For an image on the backside of the business card it can be a photo, hand-drawn or whatever but it must visually combine coffee and cycling in some way. The interior of the Coffee House will be reclaimed wood, rustic and have an urban feel to it with cycling artifacts hanging from the walls/ceiling, etc. Finally, it would be beneficial if the business card design elements can be easily used on flyers and other promotional assets. Good luck, we are looking forward to seeing your creative ideas.

Target Market(s)

Coffee lovers and cycling fans

Contact Information for Business Card

See project description.

Colors

Designer to choose colors to be used in the design.

Requirements
Must have
• Must use the current logo provided and combine a coffee and bike theme.
Nice to have
• Orange is used in current logo and could be used as an accent color on the backside of the business card.

```html
<!DOCTYPE html>
<html lang="en">
<head>
<meta charset="utf-8">
<title>RM Coffee House – Business Card</title>
<link rel="stylesheet" href="https://fonts.googleapis.com/css2?family=Open+Sans:wght@600&display=swap">
<style>
  :root {
    --page: #ffffff;
    --deep-teal: #0c3050;
    --ink: #10171f;
    --navy: #1e2d48;
    --navy-soft: #1a2844;
    --orange: #ea6640;
    --orange-light: #f2814a;
    --orange-dark: #b84a28;
    --brand-orange: #f26a24;
  }
  html, body {
    margin: 0;
    width: 1200px;
    height: 714px;
    overflow: hidden;
    background: var(--page);
  }
  .card {
    position: absolute;
    left: 45px;
    top: 38px;
    width: 1113px;
    height: 636px;
    overflow: hidden;
  }
  .card-art {
    position: absolute;
    inset: 0;
    width: 100%;
    height: 100%;
    display: block;
  }
  .brand {
    position: absolute;
    left: 519px;
    top: 165px;
    width: 440px;
    margin: 0;
    text-align: center;
    font-family: "Open Sans", sans-serif;
    font-weight: 600;
    color: var(--brand-orange);
  }
  .brand-initials {
    display: block;
    font-size: 200px;
    line-height: 200px;
    letter-spacing: 4px;
  }
  .brand-descriptor {
    display: block;
    margin-top: 42px;
    font-size: 40px;
    line-height: 48px;
    letter-spacing: 2px;
  }
</style>
</head>
<body>
  <div class="card">
    <svg class="card-art" viewBox="0 0 1050 600" preserveAspectRatio="none" aria-hidden="true">
      <defs>
        <linearGradient id="bg-fade" x1="0" y1="0" x2="1" y2="0">
          <stop offset="0" stop-color="var(--deep-teal)"/>
          <stop offset="1" stop-color="var(--ink)"/>
        </linearGradient>
        <linearGradient id="sweep-fade" x1="0" y1="0" x2="1" y2="0">
          <stop offset="0" stop-color="var(--deep-teal)" stop-opacity="0.9"/>
          <stop offset="0.55" stop-color="var(--deep-teal)" stop-opacity="0.35"/>
          <stop offset="1" stop-color="var(--ink)" stop-opacity="0"/>
        </linearGradient>
        <linearGradient id="band-orange" x1="0" y1="0" x2="1" y2="0">
          <stop offset="0" stop-color="#f38549"/>
          <stop offset="1" stop-color="#ec6040"/>
        </linearGradient>
        <linearGradient id="slab-orange" x1="0" y1="1" x2="1" y2="0">
          <stop offset="0" stop-color="#f07a45"/>
          <stop offset="0.5" stop-color="#e96440"/>
          <stop offset="1" stop-color="#e96440"/>
        </linearGradient>
        <linearGradient id="fold" x1="0" y1="0" x2="1" y2="1">
          <stop offset="0" stop-color="var(--orange-dark)"/>
          <stop offset="1" stop-color="#e0703a"/>
        </linearGradient>
      </defs>

      <rect class="backdrop" width="1050" height="600" fill="url(#bg-fade)"/>
      <rect class="backdrop-stripe" x="0" y="98" width="1050" height="386" fill="var(--navy-soft)" opacity="0.55"/>
      <path class="lower-sweep" d="M150,600 C210,515 250,484 310,484 L1050,484 L1050,600 Z" fill="url(#sweep-fade)"/>

      <path class="navy-panel" d="M488,98 L1050,98 L1050,434 L280,454 Q262,454 272,436 Z" fill="var(--navy)"/>

      <path class="orange-slab" d="M0,165 Q55,32 158,32 L526,36 L93,600 L0,600 Z" fill="url(#slab-orange)"/>
      <polygon class="orange-fold" points="526,36 578,98 488,98" fill="url(#fold)"/>

      <path class="orange-band" d="M303,527 Q370,434 450,434 L1050,434 L1050,527 Z" fill="url(#band-orange)"/>
      <path class="orange-tab" d="M938,411 Q962,370 1000,370 L1050,370 L1050,411 Z" fill="var(--orange-light)"/>
    </svg>

    <h1 class="brand">
      <span class="brand-initials">RM</span>
      <span class="brand-descriptor">COFFEE HOUSE</span>
    </h1>
  </div>
</body>
</html>
```